Larkmoor Health- Core Values Graphic for Visual Appeal

I would like a poster that could take these written core values from our organization and create a graphic that we could use for our staff and employees. I would also like to incorporate our branding into this project. Thank you!

Target Market(s)

To helps patients and employees understand the core values of our organization

Industry/Entity Type

Healthcare

Requirements
Must have
• Match our branding
Nice to have
• Please use your creativity!
Should not have
• Overly complex/ busy

```html
<!DOCTYPE html>
<html lang="en">
<head>
<meta charset="utf-8">
<title>Larkmoor Health – These Core Values</title>
<link rel="stylesheet" href="https://fonts.googleapis.com/css2?family=Poppins:wght@400;500;600;700;800&display=swap">
<style>
  :root {
    --ink: #2b2b2f;
    --slate: #3d3d42;
    --blue: #1e9ee6;
    --blue-dark: #1478b8;
    --white: #ffffff;
    --paper: #ffffff;
  }
  * { box-sizing: border-box; margin: 0; padding: 0; }
  html, body { width: 667px; height: 1200px; overflow: hidden; background: var(--paper); }
  body { font-family: "Poppins", Arial, sans-serif; color: var(--ink); position: relative; }

  .header { position: absolute; top: 30px; left: 24px; right: 24px; display: flex; gap: 16px; }
  .brand { width: 150px; display: flex; flex-direction: column; align-items: center; justify-content: center; gap: 8px; }
  .brand-dot { width: 46px; height: 46px; border-radius: 50%; background: var(--blue); }
  .brand-name { font-weight: 700; font-size: 19px; color: var(--blue-dark); line-height: 1.1; text-align: center; }
  .intro { flex: 1; }
  .title { font-weight: 800; font-size: 52px; line-height: 1; letter-spacing: -0.5px; color: var(--ink); }
  .lede { margin-top: 10px; font-size: 14.5px; line-height: 1.45; color: var(--blue-dark); font-weight: 500; }

  .value { position: absolute; width: 298px; border-radius: 22px; padding: 24px 22px; color: var(--white); }
  .value.blue { background: var(--blue); }
  .value.slate { background: var(--slate); }
  .family { left: 24px; top: 228px; height: 397px; }
  .excellence { left: 345px; top: 228px; height: 397px; }
  .service { left: 24px; top: 655px; height: 400px; }
  .integrity { left: 345px; top: 655px; height: 400px; }

  .value-head { display: flex; align-items: center; gap: 10px; margin-bottom: 12px; }
  .value-icon { width: 26px; height: 26px; border-radius: 50%; background: var(--white); position: relative; flex: none; }
  .value-icon::after { content: ""; position: absolute; inset: 8px; border-radius: 50%; background: var(--blue); }
  .value-name { font-weight: 800; font-size: 27px; letter-spacing: 0.5px; }
  .value-text { font-size: 13.5px; line-height: 1.45; }
  .value-text.right { text-align: right; }
  .notch { width: 100px; height: 100px; shape-outside: circle(100px at 0 0); }
  .service .notch { float: right; shape-outside: circle(100px at 100% 0); margin: -24px -22px 0 0; }
  .integrity .notch { float: left; shape-outside: circle(100px at 0 0); margin: -24px 0 0 -22px; }

  .hub { position: absolute; left: 333.5px; top: 640px; width: 170px; height: 170px; transform: translate(-50%, -50%); }

  .site { position: absolute; left: 0; right: 0; top: 1100px; text-align: center; font-weight: 700; font-size: 22px; letter-spacing: 3px; color: var(--blue-dark); }
</style>
</head>
<body>
  <header class="header">
    <div class="brand">
      <span class="brand-dot"></span>
      <span class="brand-name">Larkmoor Health</span>
    </div>
    <div class="intro">
      <h1 class="title">THESE CORE VALUES</h1>
      <p class="lede">Are the spirit of who we are as a healthcare team. They guide our actions, unite us in purpose, and ensure that we provide world-class care while fostering a positive and supportive atmosphere within our team.</p>
    </div>
  </header>

  <section class="value blue family">
    <div class="value-head"><span class="value-icon"></span><h2 class="value-name">FAMILY</h2></div>
    <p class="value-text">At the heart of our mission is the commitment to provide high-quality, affordable healthcare in a comforting and uplifting family-oriented environment. Just as our community is our extended family, every patient is a cherished member of our healthcare family. We treat each individual with the same care, compassion, and respect we would offer to our own loved ones.</p>
  </section>

  <section class="value slate excellence">
    <div class="value-head" style="justify-content:flex-end"><h2 class="value-name">EXCELLENCE</h2><span class="value-icon"></span></div>
    <p class="value-text right">In line with our goal, we aspire not only to alleviate pain but also to inspire patients to become active participants in their well-being. We believe in empowering our patients through education and compassion. Our pursuit of excellence is unwavering, driven by our dedication to continuously improve our services at every level, ensuring that our community receives nothing less than exceptional care.</p>
  </section>

  <section class="value slate service">
    <div class="notch"></div>
    <div class="value-head"><span class="value-icon"></span><h2 class="value-name">SERVICE</h2></div>
    <p class="value-text">Our vision is grounded in the belief that every person possesses the innate potential for true health. We aim to facilitate the body's natural healing response by providing the highest level of service. Our hope for each patient extends beyond healing; we aspire to help you fulfill your life's mission and purpose abundantly, supporting you in your journey to well-being.</p>
  </section>

  <section class="value blue integrity">
    <div class="notch"></div>
    <div class="value-head" style="justify-content:flex-end"><h2 class="value-name">INTEGRITY</h2><span class="value-icon"></span></div>
    <p class="value-text right">In our healthcare team, 'integrity' is non-negotiable. Our purpose is deeply rooted in ethics, integrity, and professional standards. We operate with the utmost integrity in every aspect of our work, adhering to the highest ethical principles. We understand that trust is the foundation of healthcare, and we are committed to maintaining the trust our community places in us.</p>
  </section>

  <svg class="hub" viewBox="0 0 170 170" aria-hidden="true">
    <circle cx="85" cy="85" r="84" fill="var(--white)"/>
    <circle cx="85" cy="85" r="70" fill="none" stroke="var(--blue)" stroke-width="10"/>
    <circle cx="85" cy="85" r="54" fill="none" stroke="var(--slate)" stroke-width="4"/>
  </svg>

  <p class="site">www.larkmoorhealth.com</p>
</body>
</html>
```